stickers for outdoor industry (brands like Veltrana, Kelso, Marlin) retail consultant

The main need that I need to solve: I am hosting a series of educational workshops at a trade show and I need a 2.5" diameter round sticker designed with my visual branding. In some additional designs, I'd like to see other shapes/sizes that occupy 4-8 sq inches of space.I am a specialty/independent retail consultant and I help small/local retailers run a more profitable business. My industry focus is on outdoor retailers (like small versions DTU) and the sticker is to be passed out at the main tradeshow that our industry has (think brands like Veltrana, Bivo, Kelso, Marlin, etc) I plan to put the stickers on the seats in the workshop and hope the attendees attach them to their water bottles, coolers, beer fridges, etc.I have the fonts and the background image--I just need some help with design, content, and the file to submit to the sticker printer. The name of my company is Hollow Pines (hollowpines.com to learn more). I need to use fonts Lulo Clean One Bold and Avenir Next LT Pro Light, which I have the permissions for.
I attached a mock up that is my vibe...but I'm open to other designs as well.
Updates
I'm also launching an industry networking group called THE GATHERING and would like a 2.5" round sticker design with the words "the gathering by hollow pines" "a community for specialty retailers" and/or other language from https://www.hollowpines.com/thegathering
Target Market(s)
retail buyers and owners of specialty outdoor retail shops; sales representatives of merchandise/brands that these retailers buy from. we buy/sell merchandise to aid our adventures in camping, hiking, trail running, global/adventure/urban travel, mountaineering, fishing, kayaking, SUP, etc
Industry/Entity Type
Retail
Font styles to use
Other font styles liked:
- lulo clean one bold, avenir next LTF light
Requirements
Must have
- -file that looks nice on 2.5" round sticker
- -other various designs that fit my target market
- -inspriational feel
- -a mix of my visual branding + your visual branding ideas if you're inspired
- -"HOLLOW PINES"
- -"hollowpines.com"
Nice to have
- Design 1) "resources for specialty retailers"
- Design 2) "support small business" or "support your local shop"
- Design 3) "THE GATHERING by HOLLOW PINES" "a community for specialty retailers"
- I like images that have sun rays or a wash of light in them
- maybe a few designs that have outdoorsy images or recreational activities in them
Should not have
- the words: consultant, consulting, agency, firm

```html
<!DOCTYPE html>
<html lang="en">
<head>
<meta charset="utf-8">
<title>Hollow Pines — Sticker Set</title>
<link rel="stylesheet" href="https://fonts.googleapis.com/css2?family=Montserrat:wght@300;400;700;800&display=swap">
<style>
  :root {
    --page: #ffffff;
    --ink: #1c1b20;
    --white: #ffffff;
    --teal-ink: #2c6f8c;
    --aqua-1: #b9e6ea;
    --aqua-2: #d9eeee;
    --aqua-3: #7fc9cf;
    --dusk-1: #5d4f86;
    --dusk-2: #e9855a;
    --dusk-3: #2b2a2a;
    --lake-1: #cfe5de;
    --lake-2: #3f93a3;
    --lake-3: #1c4f6e;
    --gold-1: #f2dcc0;
    --gold-2: #d59a4f;
    --gold-3: #b9862d;
  }
  * { box-sizing: border-box; margin: 0; padding: 0; }
  html, body { width: 1200px; height: 1200px; overflow: hidden; background: var(--page); }
  .canvas { position: relative; width: 1200px; height: 1200px; }

  .sticker {
    position: absolute; width: 360px; height: 360px;
    border-radius: 50%; overflow: hidden;
    font-family: "Montserrat", sans-serif; text-align: center;
  }
  .sticker--resources { left: 222px; top: 220px; }
  .sticker--support-small { left: 612px; top: 220px; }
  .sticker--gathering { left: 222px; top: 610px; }
  .sticker--support-local { left: 612px; top: 610px; }

  .sticker__art { position: absolute; inset: 0; width: 100%; height: 100%; }
  .sticker__frame { position: absolute; inset: 0; width: 100%; height: 100%; }
  .sticker__frame path { fill: none; stroke: var(--white); stroke-width: 2.5; }

  .tagline {
    position: absolute; left: 0; right: 0; top: 58px;
    font-weight: 300; font-size: 15.5px; letter-spacing: 0.2em; line-height: 24px;
    text-transform: uppercase;
  }
  .tagline--bold {
    top: 38px; font-weight: 700; font-size: 20px; line-height: 25px; letter-spacing: 0.18em;
    color: var(--teal-ink);
  }
  .wordmark {
    position: absolute; left: 0; right: 0; top: 138px;
    font-weight: 800; font-size: 40px; line-height: 49px; letter-spacing: 0.3em;
    padding-left: 0.3em; text-transform: uppercase;
  }
  .rule { position: absolute; left: 96px; width: 168px; top: 270px; height: 2px; }
  .site {
    position: absolute; left: 0; right: 0; top: 276px;
    font-weight: 700; font-size: 12.5px; letter-spacing: 0.14em; text-transform: uppercase;
  }
  .socials { position: absolute; left: 0; right: 0; top: 298px; display: flex; justify-content: center; gap: 6px; }
  .socials span { width: 13px; height: 13px; border-radius: 50%; }

  .tone-dark { color: var(--ink); }
  .tone-dark .rule, .tone-dark .socials span { background: var(--ink); }
  .tone-light { color: var(--white); }
  .tone-light .rule, .tone-light .socials span { background: var(--white); }
  .sticker--gathering .wordmark, .sticker--gathering .site { color: var(--white); }
</style>
</head>
<body>
<div class="canvas">

  <!-- Sticker 1 -->
  <div class="sticker sticker--resources tone-dark">
    <svg class="sticker__art" viewBox="0 0 360 360" role="img" aria-label="Misty mountain ridges under a soft aqua sky with a wash of light">
      <defs><linearGradient id="g-aqua" x1="0" y1="0" x2="0" y2="1">
        <stop offset="0" stop-color="var(--aqua-1)"/><stop offset="0.5" stop-color="var(--aqua-2)"/><stop offset="1" stop-color="var(--aqua-3)"/>
      </linearGradient></defs>
      <rect width="360" height="360" fill="url(#g-aqua)"/>
    </svg>
    <svg class="sticker__frame" viewBox="0 0 360 360" aria-hidden="true">
      <path d="M41.4 100 A160 160 0 0 1 318.6 100"/><path d="M41.4 260 A160 160 0 0 0 318.6 260"/>
    </svg>
    <p class="tagline">Resources for<br>specialty retailers</p>
    <h2 class="wordmark">Hollow<br>Pines</h2>
    <div class="rule"></div>
    <p class="site">hollowpines.com</p>
    <div class="socials"><span></span><span></span><span></span></div>
  </div>

  <!-- Sticker 2 -->
  <div class="sticker sticker--support-small tone-light">
    <svg class="sticker__art" viewBox="0 0 360 360" role="img" aria-label="Snowy mountain peak reflected in a lake at sunset, pine forest shoreline">
      <defs><linearGradient id="g-dusk" x1="0" y1="0" x2="0" y2="1">
        <stop offset="0" stop-color="var(--dusk-1)"/><stop offset="0.3" stop-color="var(--dusk-2)"/><stop offset="0.45" stop-color="var(--dusk-3)"/><stop offset="0.65" stop-color="var(--dusk-2)"/><stop offset="1" stop-color="var(--dusk-3)"/>
      </linearGradient></defs>
      <rect width="360" height="360" fill="url(#g-dusk)"/>
    </svg>
    <svg class="sticker__frame" viewBox="0 0 360 360" aria-hidden="true">
      <path d="M41.4 100 A160 160 0 0 1 318.6 100"/><path d="M41.4 260 A160 160 0 0 0 318.6 260"/>
    </svg>
    <p class="tagline">Support<br>small business</p>
    <h2 class="wordmark">Hollow<br>Pines</h2>
    <div class="rule"></div>
    <p class="site">hollowpines.com</p>
    <div class="socials"><span></span><span></span><span></span></div>
  </div>

  <!-- Sticker 3 -->
  <div class="sticker sticker--gathering tone-light">
    <svg class="sticker__art" viewBox="0 0 360 360" role="img" aria-label="Layered teal mountains over a calm lake with light haze">
      <defs><linearGradient id="g-lake" x1="0" y1="0" x2="0" y2="1">
        <stop offset="0" stop-color="var(--lake-1)"/><stop offset="0.45" stop-color="var(--lake-2)"/><stop offset="1" stop-color="var(--lake-3)"/>
      </linearGradient></defs>
      <rect width="360" height="360" fill="url(#g-lake)"/>
    </svg>
    <svg class="sticker__frame" viewBox="0 0 360 360" aria-hidden="true">
      <path d="M41.4 100 A160 160 0 0 1 318.6 100"/><path d="M41.4 260 A160 160 0 0 0 318.6 260"/>
    </svg>
    <p class="tagline tagline--bold">The<br>Gathering<br>by</p>
    <h2 class="wordmark">Hollow<br>Pines</h2>
    <div class="rule"></div>
    <p class="site">hollowpines.com</p>
    <div class="socials"><span></span><span></span><span></span></div>
  </div>

  <!-- Sticker 4 -->
  <div class="sticker sticker--support-local tone-dark">
    <svg class="sticker__art" viewBox="0 0 360 360" role="img" aria-label="Golden meadow with soft sunlight and blurred bokeh glow">
      <defs><radialGradient id="g-gold" cx="0.5" cy="0.35" r="0.7">
        <stop offset="0" stop-color="var(--gold-1)"/><stop offset="0.6" stop-color="var(--gold-2)"/><stop offset="1" stop-color="var(--gold-3)"/>
      </radialGradient></defs>
      <rect width="360" height="360" fill="url(#g-gold)"/>
    </svg>
    <svg class="sticker__frame" viewBox="0 0 360 360" aria-hidden="true">
      <path d="M41.4 100 A160 160 0 0 1 318.6 100"/><path d="M41.4 260 A160 160 0 0 0 318.6 260"/>
    </svg>
    <p class="tagline">Support<br>your local shop</p>
    <h2 class="wordmark">Hollow<br>Pines</h2>
    <div class="rule"></div>
    <p class="site">hollowpines.com</p>
    <div class="socials"><span></span><span></span><span></span></div>
  </div>

</div>
</body>
</html>
```